Flyer Design Project

We are offering a new class on cyber crime and want to advertise this course to students. We would like to see a design that is eye catching and coveys the goals of the course, when it meets and a brief abstract for the class.

The course will focus on the economics of cyber crime so including one or two graphics that get across this point would be good.

Requirements
Must have
• Course name "Cyber Crime"
Call number "CS 795 - 004"
Course meeting time (day of week and time) Tue. 4:30-7:10pm
Course goals
Course abstract

```html
<!DOCTYPE html>
<html lang="en">
<head>
<meta charset="utf-8">
<title>Cyber Crime – Course Flyer</title>
<link rel="stylesheet" href="https://fonts.googleapis.com/css2?family=Arimo:wght@400;700&family=Questrial&display=swap">
<style>
  :root {
    --black: #000000;
    --white: #ffffff;
    --yellow: #fff200;
    --title-yellow: #ffff1a;
    --red: #e8101a;
    --red-dark: #b0000c;
    --tab-red: #d9101c;
    --tab-orange: #f3341c;
    --photo-dark: #1a1a1a;
    --photo-mid: #6f6f6f;
    --photo-light: #e9e9e9;
  }
  * { margin: 0; padding: 0; box-sizing: border-box; }
  html, body { width: 929px; height: 1200px; overflow: hidden; background: var(--white); }
  .flyer {
    position: relative;
    width: 929px;
    height: 1200px;
    overflow: hidden;
    background: var(--yellow);
    font-family: "Questrial", "Century Gothic", sans-serif;
    color: var(--black);
  }
  .masthead {
    position: absolute;
    left: 0; top: 0;
    width: 929px; height: 167px;
    background: var(--black);
  }
  .course-title {
    position: absolute;
    left: 0; top: 24px;
    width: 929px;
    text-align: center;
    font-family: "Arimo", Arial, sans-serif;
    font-weight: 700;
    font-size: 100px;
    line-height: 120px;
    letter-spacing: -1px;
    color: var(--title-yellow);
    -webkit-text-stroke: 9px var(--red);
    paint-order: stroke fill;
  }
  .details-bar {
    position: absolute;
    left: 0; top: 167px;
    width: 929px; height: 75px;
    background: var(--black);
    border-top: 1.5px solid var(--white);
    border-bottom: 1.5px solid var(--white);
    color: var(--white);
    font-family: "Arimo", Arial, sans-serif;
  }
  .detail { position: absolute; top: 13px; }
  .detail--number { left: 120px; }
  .detail--time { left: 391px; }
  .detail-label { font-weight: 700; font-size: 19px; line-height: 24px; }
  .detail-value { font-size: 16px; line-height: 22px; margin-top: 8px; }
  .section-heading {
    position: absolute;
    left: 0;
    height: 31px;
    display: flex;
  }
  .section-heading::before {
    content: "";
    width: 45px;
    height: 100%;
    background: var(--red-dark);
  }
  .section-heading span {
    display: block;
    height: 100%;
    padding: 0 12px 0 14px;
    background: linear-gradient(90deg, var(--tab-red), var(--tab-orange));
    color: var(--white);
    font-family: "Arimo", Arial, sans-serif;
    font-weight: 700;
    font-size: 23px;
    line-height: 31px;
  }
  .section-heading--goals { top: 251px; }
  .section-heading--goals span { width: 281px; }
  .section-heading--abstract { top: 393px; }
  .section-heading--abstract span { width: 231px; background: linear-gradient(90deg, var(--tab-orange), #f5501e); }
  .goals-list {
    position: absolute;
    left: 58px; top: 293px;
    width: 600px;
    list-style: none;
    font-size: 16.5px;
    line-height: 16px;
  }
  .goals-list li + li { margin-top: 13px; }
  .abstract-text {
    position: absolute;
    left: 58px; top: 426px;
    width: 806px;
    font-size: 16px;
    line-height: 20.5px;
    text-align: justify;
  }
  .hero-visual {
    position: absolute;
    left: 0; top: 561px;
    width: 929px; height: 578px;
    background:
      radial-gradient(ellipse 38% 42% at 50% 48%, var(--photo-light) 0%, #b9b9b9 35%, rgba(80,80,80,0) 75%),
      linear-gradient(180deg, var(--photo-dark) 0%, var(--photo-mid) 45%, #2c2c2c 100%);
  }
  .footer-band {
    position: absolute;
    left: 0; top: 1139px;
    width: 929px; height: 61px;
    background: var(--yellow);
    text-align: center;
    font-family: "Arimo", Arial, sans-serif;
    font-weight: 700;
    font-size: 25px;
    line-height: 61px;
  }
</style>
</head>
<body>
<main class="flyer">
  <header class="masthead">
    <h1 class="course-title">Cyber Crime</h1>
  </header>

  <section class="details-bar">
    <div class="detail detail--number">
      <div class="detail-label">Cource Number</div>
      <div class="detail-value">CS 795 / ISA 797</div>
    </div>
    <div class="detail detail--time">
      <div class="detail-label">Course Meeting Time</div>
      <div class="detail-value">Fall 2012 (day of week and time) Tue. 4:30-7:10pm</div>
    </div>
  </section>

  <h2 class="section-heading section-heading--goals"><span>The Goal of the Class</span></h2>
  <ol class="goals-list">
    <li>1) Understand how modern cyber-crime operates on a technical and economic level.</li>
    <li>2) Analyze some of the potential places to intervene at an economic, technical and policy level.</li>
  </ol>

  <h2 class="section-heading section-heading--abstract"><span>Course Abstract</span></h2>
  <p class="abstract-text">Arguably the single most significant change in the cyber-security landscape has been the explosive rise of profit-fueled cyber-crime. Obtaining a detailed, structural understanding of how profit-driven cyber crime works — its underlying economics and associated business practices — has the potential to illuminate new defensive measures that might prove far more efficient for countering attacks than purely technical measures. This research seminar will delve into our current understanding of the economics of cyber-crime.</p>

  <div class="hero-visual" role="img" aria-label="Black and white photo of a computer monitor showing a globe, with keyboard and mouse, surrounded by bursting light and streams of binary digits"></div>

  <footer class="footer-band">http://cs.northfield.edu/~hale/crime.html</footer>
</main>
</body>
</html>
```